Redesign for luxury lifestyle PR agency

Ginger Kite Otter is a luxury lifestyle public relations agency specialising in indigenous and regenerative travel. We are the elephant you want in the room. We represent interesting brands and people who would be described as changemakers in their respective fields. The winning design should be stylish, clean cut and earthy. It should communicate that Ginger Kite Otter is professional and representative of the industries that it serves. The purpose of the website is to provide clear information to potential customers and media, improve the image and brand of the company, position the company as one of scale and increase sales conversions. Its aesthetic will be aspirational and image led in an editorial style. I would like to be able to easily edit the website once finished and be able to work with the designer on an ad hoc basis once the project is completed.

Please see below for some website I like the style of:

https://www.velmora-ensemble.com/

https://www.tasbergglobal.com/

https://www.brindlequarterly.co.uk/

Pages I would like to include are:

Home
Services
Clients
Testimonials
About Us
News

I'm also attaching a proposal that I really liked the style of and I would like this sort of aesthetic on the website too. My logo is also attached (it is likely that the colour palette might change with the website).

I'm open to inspiration on the colours - my immediate preference is greens and/or blues.

Here is the existing website that I built myself on Wix - https://www.gingerkiteotter.com/ (it looks so outdated and amateur now hence the need of a serious rebrand)

Target Market(s)

Luxury travel and lifestyle brands

Industry/Entity Type

Luxury travel and lifestyle

Number of Pages Required

1 page

Font styles to use
Serif
Other font styles liked:
• Open to suggestions

Requirements
Must have
• Beautiful imagery

```html
<!DOCTYPE html>
<html lang="en">
<head>
<meta charset="utf-8">
<title>Ginger Kite Otter — Lifestyle PR</title>
<link rel="stylesheet" href="https://fonts.googleapis.com/css2?family=Playfair+Display:wght@400;500;600&family=Poppins:wght@300;400;500&display=swap">
<style>
:root{
  --navy:#2b3081;
  --navy-deep:#232870;
  --blue:#1b78c6;
  --cyan:#1aa3dc;
  --ice:#e5f3fa;
  --ink:#2a2f6e;
  --grey:#666a7a;
  --yellow:#f6d10a;
  --white:#ffffff;
  --serif:"Playfair Display",Georgia,serif;
}
*{margin:0;padding:0;box-sizing:border-box}
html,body{width:1200px;height:4304px;overflow:hidden}
body{position:relative;background:var(--white);font-family:"Poppins",sans-serif;color:var(--ink)}
.abs{position:absolute}
.heading{font-family:var(--serif);font-weight:400;color:var(--navy);letter-spacing:1px}

/* navigation */
.site-nav{top:0;left:0;width:1200px;height:90px;background:var(--white)}
.site-nav a{position:absolute;top:36px;font-size:12px;color:var(--ink);text-decoration:none}
.site-nav a.active{color:var(--cyan)}
.site-nav a.active::after{content:"";position:absolute;left:0;right:0;bottom:-8px;height:2px;background:var(--cyan)}
.brand{left:520px;top:30px;width:160px;text-align:center;font-family:var(--serif);font-size:15px;line-height:17px;color:var(--blue);letter-spacing:1px}
.brand-dot{left:592px;top:8px;width:16px;height:16px;border-radius:50%;background:var(--blue)}

/* hero */
.hero{top:90px;left:0;width:1200px;height:624px;clip-path:polygon(0 0,1200px 0,1200px 550px,0 624px);
  background:
    radial-gradient(ellipse 420px 260px at 810px 330px,rgba(245,246,250,.95) 0%,rgba(220,226,236,.75) 40%,rgba(220,226,236,0) 75%),
    radial-gradient(ellipse 520px 120px at 1050px 300px,rgba(240,120,70,.85) 0%,rgba(240,120,70,0) 70%),
    radial-gradient(ellipse 700px 300px at 250px 120px,rgba(120,160,200,.8) 0%,rgba(120,160,200,0) 70%),
    linear-gradient(180deg,#6f8fad 0%,#9aa9bb 28%,#c79784 44%,#40506a 58%,#1d2a38 78%,#141c26 100%)}
.hero-title{left:62px;top:234px;font-family:var(--serif);font-weight:600;font-size:56px;line-height:62px;color:var(--white)}
.hero-box{left:50px;top:374px;width:471px;height:77px;background:rgba(41,158,214,.85);color:var(--white);font-size:14px;line-height:22px;padding:16px 0 0 12px}
.hero-arrow{left:1099px;width:42px;height:42px;border-radius:50%;background:rgba(70,70,80,.75)}

/* services */
.svc-title{top:758px;left:0;width:1200px;text-align:center;font-size:34px}
.svc-sub{top:820px;left:0;width:1200px;text-align:center;font-family:var(--serif);font-size:23px;color:var(--cyan)}
.svc-desc{top:862px;left:370px;width:460px;text-align:center;font-size:11px;line-height:22px;color:var(--grey)}
.card{width:211px;height:209px;background:var(--white);border-radius:60px 0 0 0;box-shadow:0 2px 10px rgba(40,50,110,.1);text-align:center}
.card svg{position:absolute;left:75px;top:48px}
.card p{position:absolute;left:0;right:0;top:138px;font-size:16px;line-height:22px;color:var(--navy)}
.card.featured{background:linear-gradient(135deg,#1a9ad9,#2a2f83);border-radius:0}
.card.featured p{color:var(--white)}

/* clients */
.clients-panel{top:1467px;left:0;width:449px;height:451px;background:var(--ice)}
.clients-photo{top:1467px;left:449px;width:751px;height:451px;
  background:
    radial-gradient(ellipse 220px 80px at 200px 250px,rgba(214,196,160,.95) 0%,rgba(180,160,120,.7) 45%,rgba(180,160,120,0) 80%),
    radial-gradient(ellipse 320px 50px at 560px 150px,rgba(240,240,236,.9) 0%,rgba(240,240,236,0) 80%),
    radial-gradient(ellipse 600px 90px at 400px 95px,rgba(150,160,160,.8) 0%,rgba(150,160,160,0) 80%),
    linear-gradient(180deg,#c4d9ea 0%,#a6c2d8 18%,#6e8e9e 26%,#2f8fc9 34%,#1b78b4 55%,#0f5b93 78%,#0a3f6c 100%)}
.circle-btn{width:44px;height:44px;border-radius:50%;border:1.5px solid var(--cyan);background:var(--white)}
.circle-btn svg{position:absolute;left:14px;top:13px}
.client-name{left:491px;top:1778px;font-family:var(--serif);font-size:34px;color:#35b9e8}
.client-text{left:494px;top:1830px;width:540px;font-size:11px;line-height:20px;color:var(--white)}
.client-link{left:1116px;top:1845px;font-size:10px;color:var(--yellow);text-decoration:underline}

/* projects */
.projects{top:1918px;left:0;width:1200px;height:415px;background:var(--navy)}
.projects h2{position:absolute;top:74px;width:1200px;text-align:center;font-family:var(--serif);font-weight:400;font-size:23px;color:#dfe3f5;letter-spacing:1px}
.thumb{top:2050px;width:135px;height:134px}
.dark-btn{width:40px;height:40px;border-radius:50%;border:1.5px solid #5aa6e0}
.dark-btn svg{position:absolute;left:13px;top:12px}

/* testimonials */
.tst-title{top:2398px;left:0;width:1200px;text-align:center;font-size:34px}
.avatar-ring{top:2466px;left:546px;width:108px;height:108px;border-radius:50%;border:2px solid var(--cyan);background:var(--white)}
.avatar{top:2474px;left:554px;width:92px;height:92px;border-radius:50%;background:radial-gradient(circle at 50% 40%,#d8b49a 0%,#8a5a42 45%,#cfe0ea 75%)}
.tst-text{top:2608px;left:276px;width:648px;text-align:center;font-size:12.5px;line-height:22.5px;color:var(--grey)}
.tst-name{top:2727px;left:0;width:1200px;text-align:center;font-size:16px;color:var(--navy)}
.tst-role{top:2752px;left:0;width:1200px;text-align:center;font-size:15px;color:var(--cyan)}

/* about */
.about-photo{top:2849px;left:0;width:750px;height:486px;
  background:
    radial-gradient(ellipse 260px 420px at 80px 220px,rgba(40,60,52,.95) 0%,rgba(40,60,52,0) 80%),
    radial-gradient(ellipse 220px 300px at 640px 120px,rgba(70,110,60,.9) 0%,rgba(70,110,60,0) 80%),
    radial-gradient(ellipse 380px 220px at 330px 200px,rgba(140,160,155,.8) 0%,rgba(140,160,155,0) 80%),
    linear-gradient(180deg,#b5ccd4 0%,#8aa5a6 30%,#5d7a72 55%,#3e5c5c 75%,#2b4547 100%)}
.about-bg{top:2849px;left:750px;width:450px;height:486px;background:var(--ice)}
.about-box{top:2916px;left:632px;width:538px;height:351px;background:var(--ice)}
.about-accent{top:3125px;left:401px;width:127px;height:142px;background:var(--blue)}
.portrait{top:2939px;left:433px;width:202px;height:304px;background:radial-gradient(ellipse 90px 120px at 100px 120px,#cfcfcf 0%,#8d8d8d 55%,#3c3c3c 100%)}
.about-title{top:2950px;left:673px;font-size:37px}
.about-text{top:3006px;left:673px;width:430px;font-size:11px;line-height:20.7px;color:var(--grey)}
.about-text p+p{margin-top:11px}

/* news */
.news-title{top:3402px;left:0;width:1200px;text-align:center;font-size:34px}
.news-img{top:3484px;width:323px;height:226px}
.news-card{top:3651px;width:285px;height:180px;background:var(--white)}
.pill{position:absolute;left:16px;top:24px;padding:0 14px;height:19px;border-radius:10px;font-size:10.5px;line-height:19px;color:var(--white);background:var(--cyan)}
.pill.yellow{background:var(--yellow);color:var(--ink)}
.news-card h3{position:absolute;left:16px;top:56px;width:265px;font-weight:400;font-size:15px;line-height:22px;color:var(--ink)}
.news-card p{position:absolute;left:16px;top:112px;width:260px;font-size:10.5px;line-height:19px;color:var(--grey)}

/* footer */
.footer{top:3930px;left:0;width:1200px;height:374px;background:var(--navy);clip-path:polygon(0 14px,1200px 84px,1200px 374px,0 374px)}
.footer-stripe{top:3920px;left:0;width:1200px;height:60px;background:var(--cyan);clip-path:polygon(0 10px,1200px 68px,1200px 74px,0 17px)}
.contact-title{left:61px;top:4022px;font-family:var(--serif);font-size:34px;color:var(--white)}
.contact-sub{left:61px;top:4074px;font-size:14px;color:var(--cyan)}
.contact-row{left:60px;width:359px;height:41px;border:1.5px solid var(--cyan);color:var(--white);font-size:14px;line-height:38px;padding-left:60px}
.contact-row svg{position:absolute;left:14px;top:9px}
.copyright{top:4274px;left:0;width:1200px;text-align:center;font-size:10.5px;color:#d6daf0}
.copyright span{color:var(--cyan)}
</style>
</head>
<body>

<header class="abs site-nav">
  <a href="#" class="active" style="left:279px">Home</a>
  <a href="#" style="left:333px">Services</a>
  <a href="#" style="left:400px">Clients</a>
  <a href="#" style="left:461px">Testimonials</a>
  <span class="abs brand-dot"></span>
  <div class="abs brand">GINGER KITE<br>OTTER</div>
  <a href="#" style="left:676px">About Us</a>
  <a href="#" style="left:750px">News</a>
  <a href="#" style="left:804px">Contact Us</a>
</header>

<section class="abs hero" role="img" aria-label="Dusk photograph of a glowing translucent pavilion on a lawn with people walking past"></section>
<h1 class="abs hero-title">The Elephant You<br>Want In The Room</h1>
<div class="abs hero-box">Ginger Kite Otter is a boutique lifestyle PR and communications<br>agency helping brands get their voices heard in the UK.</div>
<div class="abs hero-arrow" style="top:323px"><svg class="abs" style="left:16px;top:14px" width="10" height="14"><path d="M8 1 2 7l6 6" stroke="#fff" stroke-width="1.5" fill="none"/></svg></div>
<div class="abs hero-arrow" style="top:369px"><svg class="abs" style="left:17px;top:14px" width="10" height="14"><path d="M2 1l6 6-6 6" stroke="#fff" stroke-width="1.5" fill="none"/></svg></div>

<h2 class="abs heading svc-title">SERVICES</h2>
<div class="abs svc-sub">Pure And Simple</div>
<p class="abs svc-desc">No-nonsense approach to launching new brands to the UK market, offering a completely bespoke service to include:</p>

<div class="abs card" style="left:254px;top:944px">
  <svg width="60" height="60" viewBox="0 0 60 60" fill="none" stroke="#2b3081" stroke-width="2"><rect x="2" y="2" width="56" height="56"/><rect x="8" y="8" width="10" height="10" fill="#1aa3dc"/><rect x="42" y="42" width="10" height="10" fill="#1aa3dc"/><rect x="25" y="25" width="10" height="10" stroke="#f6d10a"/><path d="M18 13h17v12M35 30h12v12M25 30H13v22"/></svg>
  <p>Strategic<br>Planning</p>
</div>
<div class="abs card featured" style="left:495px;top:944px">
  <svg width="60" height="60" viewBox="0 0 60 60" fill="none" stroke="#fff" stroke-width="2"><rect x="4" y="4" width="44" height="34"/><path d="M4 12h44M12 20h14M12 26h10"/><circle cx="30" cy="30" r="7"/><path d="M18 58c0-10 5-14 12-14s12 4 12 14"/><rect x="40" y="22" width="14" height="12" fill="#f6d10a" stroke="#f6d10a"/></svg>
  <p>Consumer Media<br>Relations</p>
</div>
<div class="abs card" style="left:735px;top:944px">
  <svg width="60" height="60" viewBox="0 0 60 60" fill="none" stroke="#2b3081" stroke-width="2"><circle cx="24" cy="34" r="14"/><circle cx="24" cy="34" r="6" stroke="#1aa3dc"/><path d="M24 16v-4M24 56v-4M6 34H2M46 34h-4"/><path d="M44 28V6M38 12l6-6 6 6" stroke="#1aa3dc" stroke-width="3"/></svg>
  <p>Reputation<br>Management</p>
</div>
<div class="abs card" style="left:358px;top:1185px">
  <svg width="60" height="60" viewBox="0 0 60 60" fill="none" stroke="#2b3081" stroke-width="2"><rect x="20" y="20" width="20" height="36" rx="3"/><circle cx="30" cy="32" r="4"/><rect x="4" y="8" width="12" height="9" fill="#1aa3dc" stroke="#1aa3dc"/><rect x="44" y="8" width="12" height="9" fill="#1aa3dc" stroke="#1aa3dc"/><rect x="24" y="2" width="12" height="9" stroke="#f6d10a"/><path d="M12 32v8M48 32v8"/></svg>
  <p>Influencer<br>Engagement</p>
</div>
<div class="abs card" style="left:592px;top:1185px">
  <svg width="60" height="60" viewBox="0 0 60 60" fill="none" stroke="#2b3081" stroke-width="2"><rect x="4" y="4" width="24" height="14" fill="#1aa3dc" stroke="#1aa3dc"/><rect x="30" y="10" width="24" height="14" fill="#f6d10a" stroke="#f6d10a"/><circle cx="16" cy="34" r="6"/><circle cx="42" cy="34" r="6"/><path d="M4 58c0-9 5-14 12-14s12 5 12 14M30 58c0-9 5-14 12-14s12 5 12 14"/></svg>
  <p>Creative<br>Consultation</p>
</div>

<section class="abs clients-panel">
  <h2 class="abs heading" style="left:58px;top:130px;font-size:34px">CLIENTS</h2>
  <p class="abs" style="left:60px;top:188px;width:230px;font-size:11.5px;line-height:21px;color:var(--grey)">A dynamic collection of innovative lifestyle clients that we are wholly passionate about</p>
  <div class="abs circle-btn" style="left:60px;top:281px"><svg width="10" height="16"><path d="M8 1 2 8l6 7" stroke="#2b3081" stroke-width="1.5" fill="none"/></svg></div>
  <div class="abs circle-btn" style="left:113px;top:281px"><svg width="10" height="16"><path d="M2 1l6 7-6 7" stroke="#2b3081" stroke-width="1.5" fill="none"/></svg></div>
</section>
<div class="abs clients-photo" role="img" aria-label="Aerial photograph of a rocky island village beside deep blue sea"></div>
<div class="abs client-name">Halvane PR</div>
<p class="abs client-text">Halvane PR is one of the UK's most highly regarded luxury travel PR agencies. Maren provides strategic and creative consultation across the board at Halvane from providing ideas for new business pitches to brainstorming the conceptualisation of new launches.</p>
<a class="abs client-link">Get links</a>

<section class="abs projects"><h2>PAST PROJECTS</h2></section>
<div class="abs thumb" style="left:165px;background:radial-gradient(ellipse 60px 80px at 100px 40px,#f08ac8 0%,rgba(240,138,200,0) 80%),linear-gradient(160deg,#c46bb0 0%,#8c4f86 45%,#4a2f4e 100%)" role="img" aria-label="Street facade under a pink evening sky"></div>
<div class="abs thumb" style="left:307px;background:radial-gradient(ellipse 50px 40px at 70px 50px,#f4f1ec 0%,rgba(244,241,236,0) 90%),linear-gradient(180deg,#262626 0%,#c9c3ba 45%,#a0744f 75%,#5a3a26 100%)" role="img" aria-label="Coffee being poured through a paper filter"></div>
<div class="abs thumb" style="left:449px;background:radial-gradient(ellipse 70px 40px at 70px 80px,#7fcaf0 0%,rgba(127,202,240,0) 90%),linear-gradient(180deg,#3fb0e4,#1b8fcf)" role="img" aria-label="Blue ocean scene with a paddleboard"></div>
<div class="abs thumb" style="left:593px;background:linear-gradient(180deg,#cfd8e0 0%,#b8c4a8 30%,#7f9a44 50%,#5d7b2e 75%,#4a6424 100%)" role="img" aria-label="Person leaping across a green meadow"></div>
<div class="abs thumb" style="left:735px;background:radial-gradient(ellipse 40px 60px at 70px 70px,#a58a62 0%,rgba(165,138,98,0) 90%),linear-gradient(160deg,#ece8e2,#bfb1a2)" role="img" aria-label="Model in leopard print posed in a hoop"></div>
<div class="abs thumb" style="left:877px;background:linear-gradient(180deg,#3f5e32 0%,#6c8a56 35%,#a8b49a 60%,#eeeeea 100%)" role="img" aria-label="Tropical garden with a sculpture"></div>
<div class="abs dark-btn" style="left:555px;top:2218px"><svg width="10" height="16"><path d="M8 1 2 8l6 7" stroke="#fff" stroke-width="1.5" fill="none"/></svg></div>
<div class="abs dark-btn" style="left:603px;top:2218px"><svg width="10" height="16"><path d="M2 1l6 7-6 7" stroke="#fff" stroke-width="1.5" fill="none"/></svg></div>

<h2 class="abs heading tst-title">TESTIMONIALS</h2>
<div class="abs avatar-ring"></div>
<div class="abs avatar" role="img" aria-label="Portrait photograph of the client"></div>
<div class="abs circle-btn" style="left:157px;top:2621px"><svg width="10" height="16"><path d="M8 1 2 8l6 7" stroke="#1aa3dc" stroke-width="1.5" fill="none"/></svg></div>
<div class="abs circle-btn" style="left:997px;top:2621px"><svg width="10" height="16"><path d="M2 1l6 7-6 7" stroke="#1aa3dc" stroke-width="1.5" fill="none"/></svg></div>
<p class="abs tst-text">Lorem Ipsum has been the industry's standard dummy text ever since thes, when an unknown printer took a galley of type and scrambled it to make a type specimen book. It has survived not only five centuries, but also the leap into electronic typesetting, remaining essentially unchanged. It was popularised in the with</p>
<div class="abs tst-name">Client Name</div>
<div class="abs tst-role">Business Excutive</div>

<div class="abs about-photo" role="img" aria-label="Limestone cliffs rising from a calm bay with a longtail boat"></div>
<div class="abs about-bg"></div>
<div class="abs about-box"></div>
<div class="abs about-accent"></div>
<div class="abs portrait" role="img" aria-label="Black and white portrait photograph of the agency founder"></div>
<h2 class="abs heading about-title">ABOUT US</h2>
<div class="abs about-text">
  <p>Maren Holt founded Ginger Kite Otter in 2016 after working for one of the most reputable luxury travel PR agencies in London, leading a team that launched some of the world's most iconic hotels, as well as spending time at a national newspaper. She understands what it is like to be on either side of the PR coin and what it takes to create a juicy story.</p>
  <p>Ginger Kite Otter works as an extension to your team providing a service that feels in-house. Maren prefers a direct approach and will always pick up the phone to sound out an idea and probably ask what you're planning for dinner too. The Ginger Kite Otter clients are a carefully curated list and they feel like family.</p>
</div>

<h2 class="abs heading news-title">NEWS</h2>
<div class="abs news-img" style="left:87px;background:radial-gradient(ellipse 140px 200px at 260px 140px,#4a4a4e 0%,#6a6c72 50%,rgba(106,108,114,0) 90%),linear-gradient(135deg,#c5d6e8 0%,#9fb1c6 45%,#7d8796 100%)" role="img" aria-label="Boutique storefront against a pale sky"></div>
<div class="abs news-img" style="left:439px;background:linear-gradient(180deg,#7fb3dc 0%,#c8dbe8 35%,#e9eef0 45%,#6f9e72 58%,#3f7a52 70%,#3aa0c8 85%,#2f6e8a 100%)" role="img" aria-label="Resort pool lined with palms beside the sea"></div>
<div class="abs news-img" style="left:790px;background:linear-gradient(180deg,#2f78cc 0%,#6ea2dc 30%,#a7c7e4 48%,#3e5d3a 62%,#2b4a2a 78%,#29557a 100%)" role="img" aria-label="Palm trees beside an infinity pool and mountains"></div>
<article class="abs news-card" style="left:87px"><span class="pill yellow">25 JULY 2022</span><h3>Lorem Ipsum has been Industry's Standard Dummy Text Ever.</h3><p>Lorem Ipsum has been the industry's stand dummy text ever since thwhen an unknown printer too galley type....</p></article>
<article class="abs news-card" style="left:439px"><span class="pill">25 JULY 2022</span><h3>Lorem Ipsum has been Industry's Standard Dummy Text Ever.</h3><p>Lorem Ipsum has been the industry's stand dummy text ever since thwhen an unknown printer too galley type....</p></article>
<article class="abs news-card" style="left:790px"><span class="pill">25 JULY 2022</span><h3>Lorem Ipsum has been Industry's Standard Dummy Text Ever.</h3><p>Lorem Ipsum has been the industry's stand dummy text ever since thwhen an unknown printer too galley type....</p></article>

<div class="abs footer-stripe"></div>
<footer class="abs footer"></footer>
<div class="abs contact-title">Contact</div>
<div class="abs contact-sub">The Best Relationships Start At Hello...</div>
<div class="abs contact-row" style="top:4121px"><svg width="16" height="22" fill="none" stroke="#1aa3dc" stroke-width="1.5"><rect x="2" y="1" width="12" height="20" rx="2"/><path d="M6 17h4"/></svg>+44 (0) 7700 900418</div>
<div class="abs contact-row" style="top:4171px"><svg width="22" height="18" fill="none" stroke="#1aa3dc" stroke-width="1.5"><rect x="1" y="2" width="20" height="14"/><path d="M1 2l10 8 10-8"/></svg>maren@gingerkiteotter.com</div>
<div class="abs copyright">©2022 <span>Ginger Kite Otter</span> - All rights reserved.</div>

</body>
</html>
```